New business card with our logo

we finalized our logo with the help of pixel harbor - now we need a business card using that logo. we are a metal service center providing raw steel and metal products for fabricating, contractors, artists, etc. we have the wording for the back of the card figured out (attached, no deviations from text please), just need help putting it all together.
would like the look of steel somehow incorporated in the design ... would like the black part of the logo to be steel or silver color (the S & BRANLEY)
Other font styles liked:
- calibri, arial, similar to those, modern looking
Colors
Designer to choose colors to be used in the design.
Requirements
Must have
- Back of card must haves are attached (no deviations from wording please).
- FRONT of card:
- logo
- address
- name
- office tel
- cell
- fax
- website
- address
Nice to have
- incorporate the look of steel or element of steel somehow
- names of the staff on front not in all caps, i.e. Rosvita not ROSVITA
- this industry is more industrial, not coffee or flower shop so design should be aligned with that
- design should be classic and tasteful

```html
<!DOCTYPE html>
<html lang="en">
<head>
<meta charset="utf-8">
<title>Branley Steel – Business Card</title>
<link href="https://fonts.googleapis.com/css2?family=Arimo:wght@400;700&display=swap" rel="stylesheet">
<style>
  :root {
    --page: #2b2b2d;
    --card: #1c1c1e;
    --card-edge: #262628;
    --blue: #1d74c4;
    --white: #ffffff;
    --faint: rgba(255,255,255,0.05);
  }
  * { box-sizing: border-box; margin: 0; padding: 0; }
  html, body {
    width: 1200px; height: 1189px; overflow: hidden;
    background: var(--page);
    font-family: "Arimo", Arial, sans-serif;
    color: var(--white);
  }
  .card {
    position: absolute; left: 150px;
    width: 900px; height: 514px;
    border-radius: 34px;
    background: radial-gradient(ellipse at 40% 40%, var(--card-edge), var(--card) 70%);
    box-shadow: 0 18px 40px rgba(0,0,0,0.55);
    overflow: hidden;
  }
  .card-back { top: 50px; }
  .card-front { top: 625px; }

  .decor-ring {
    position: absolute; left: -120px; top: 120px;
    width: 440px; height: 440px; border-radius: 50%;
    border: 38px solid var(--faint);
  }

  .brand { position: absolute; display: flex; align-items: center; gap: 22px; }
  .brand-dot {
    width: 120px; height: 120px; border-radius: 50%;
    border: 12px solid var(--blue); flex: none;
  }
  .brand-name {
    font-weight: 700; font-size: 62px; line-height: 0.95;
    letter-spacing: 1px; color: var(--white);
  }
  .card-back .brand { left: 240px; top: 130px; }

  .tagline {
    position: absolute; left: 240px; top: 300px;
    font-weight: 700; font-size: 22px; line-height: 1.35;
  }

  .card-front .brand { left: 80px; top: 190px; }
  .card-front .brand-dot { width: 110px; height: 110px; border-width: 11px; }
  .card-front .brand-name { font-size: 56px; }

  .divider {
    position: absolute; left: 500px; top: 90px;
    width: 3px; height: 330px; background: var(--blue);
  }
  .contact { position: absolute; left: 540px; top: 96px; }
  .person-name { font-weight: 700; font-size: 28px; letter-spacing: 0.5px; }
  .person-name .first { color: var(--blue); }
  .person-role { font-size: 21px; margin-top: 2px; }
  .contact-list { list-style: none; margin-top: 20px; }
  .contact-list li {
    display: flex; align-items: center; gap: 12px;
    font-size: 21px; height: 30px;
  }
  .contact-list svg { width: 22px; height: 22px; flex: none; }
  .address { margin-top: 14px; font-size: 21px; line-height: 1.35; }
</style>
</head>
<body>

<section class="card card-back" aria-label="Card back">
  <div class="decor-ring"></div>
  <div class="brand">
    <div class="brand-dot"></div>
    <div class="brand-name">BRANLEY<br>STEEL</div>
  </div>
  <p class="tagline">Structural Steel - Stainless &amp; Aluminum<br>Building Components - Rebar - Decking.... and more</p>
</section>

<section class="card card-front" aria-label="Card front">
  <div class="brand">
    <div class="brand-dot"></div>
    <div class="brand-name">BRANLEY<br>STEEL</div>
  </div>
  <div class="divider"></div>
  <div class="contact">
    <p class="person-name"><span class="first">DORIAN</span> HALE</p>
    <p class="person-role">Director</p>
    <ul class="contact-list">
      <li>
        <svg viewBox="0 0 24 24"><circle cx="12" cy="12" r="11" fill="none" stroke="var(--blue)" stroke-width="2"/><path d="M7 9c0-1.5 2-2 5-2s5 .5 5 2l-1.5 1.2-2-1v-.7h-3v.7l-2 1z M8 12h8l1 4H7z" fill="var(--blue)"/></svg>
        555-310-4420
      </li>
      <li>
        <svg viewBox="0 0 24 24"><circle cx="12" cy="12" r="11" fill="none" stroke="var(--blue)" stroke-width="2"/><rect x="8.5" y="6" width="7" height="12" rx="1.2" fill="none" stroke="var(--blue)" stroke-width="1.6"/></svg>
        555-310-4421
      </li>
      <li>
        <svg viewBox="0 0 24 24"><circle cx="12" cy="12" r="11" fill="var(--blue)"/><rect x="7" y="10" width="10" height="6" fill="var(--white)"/><rect x="9" y="7" width="6" height="3" fill="var(--white)"/></svg>
        555-310-4422
      </li>
      <li>
        <svg viewBox="0 0 24 24"><circle cx="12" cy="12" r="11" fill="var(--blue)"/><rect x="6.5" y="8" width="11" height="8" fill="var(--white)"/><path d="M6.5 8l5.5 4.5L17.5 8" fill="none" stroke="var(--blue)" stroke-width="1.3"/></svg>
        info@branleymetals.com
      </li>
      <li>
        <svg viewBox="0 0 24 24"><circle cx="12" cy="12" r="11" fill="var(--blue)"/><circle cx="12" cy="12" r="6" fill="none" stroke="var(--white)" stroke-width="1.2"/><path d="M6 12h12M12 6v12M8.5 8.5q3.5 3.5 0 7M15.5 8.5q-3.5 3.5 0 7" fill="none" stroke="var(--white)" stroke-width="1"/></svg>
        www.branleysteel.com
      </li>
    </ul>
    <p class="address">P.O. Box 4821<br>Foundry Road, Dayton, USA</p>
  </div>
</section>

</body>
</html>
```